KDV by Moira Tallow - Scalp Micropigmentation

I need a wordpress site designed for me, can be based off a theme, I already have a logo and the press site ready to be created, I can provide a login for you. I will be able to update it myself with content I just need the layout done as Im having trouble with it. I want to be able to add pages as needed and have a gallery for my work.

Target Market(s)

customers

Coding

Coded - Design and coding required

Number of Pages Required

5+ page

Font styles to use
Sans Serif

Colors

Designer to choose colors to be used in the design.

Requirements
Must have
• my logo, wordpress, gallery
Should not have
• shopping cart

```html
<!DOCTYPE html>
<html lang="en">
<head>
<meta charset="utf-8">
<title>KDV by Moira Tallow – Scalp Micropigmentation</title>
<link rel="stylesheet" href="https://fonts.googleapis.com/css2?family=Poppins:wght@300;400;500;600;700&display=swap">
<style>
:root{
  --ink:#222;
  --muted:#666;
  --sky:#6cbce0;
  --teal:#2fa6a0;
  --blue:#4a8fb0;
  --orange:#d46210;
  --olive:#6b6556;
  --pale:#f0f6f7;
  --band:#6ab4d8;
  --foot:#13171b;
  --foot-text:#8d949a;
  --white:#fff;
}
*{box-sizing:border-box;margin:0;padding:0}
html,body{width:1200px;height:3179px;overflow:hidden}
body{font-family:"Poppins",sans-serif;color:var(--ink);background:var(--white);position:relative}
.abs{position:absolute}
a{color:inherit;text-decoration:none}

/* header */
.site-header{position:absolute;left:0;top:0;width:1200px;height:103px;background:var(--white)}
.btn-consult{left:226px;top:13px;width:161px;height:39px;border-radius:20px;background:var(--sky);color:#123;font-size:11px;font-weight:600;display:flex;align-items:center;justify-content:center;gap:8px}
.btn-phone{left:808px;top:11px;width:160px;height:40px;border-radius:20px;background:#ddd;color:#222;font-size:12px;font-weight:600;display:flex;align-items:center;justify-content:center;gap:8px}
.brand{left:540px;top:7px;width:84px;height:86px;border:2px solid #555;display:flex;flex-direction:column;align-items:center;justify-content:center;background:var(--white)}
.brand-name{font-size:24px;font-weight:600;letter-spacing:1px;color:#222}
.brand-sub{font-size:6px;font-weight:600;color:#222;letter-spacing:.5px;margin-top:2px}
.nav{top:71px;font-size:11px;color:#333;display:flex;gap:0}
.nav a{position:absolute;white-space:nowrap}

/* hero */
.hero{left:0;top:103px;width:1200px;height:515px;background:linear-gradient(100deg,#1c2a33 0%,#3b4a52 35%,#6a6e70 60%,#3a3e42 85%,#2a2d30 100%)}
.hero-title{left:143px;top:268px;font-size:28px;font-weight:700;color:var(--white);letter-spacing:.3px}
.hero-text{left:143px;top:322px;width:640px;font-size:13px;line-height:22px;color:var(--white)}
.hero-btn{left:145px;top:398px;width:175px;height:45px;background:var(--sky);color:var(--white);font-size:14px;display:flex;align-items:center;justify-content:center}
.hero-arrow{top:322px}

/* what we do */
.section-title{width:1200px;left:0;text-align:center;font-size:18px;font-weight:700;letter-spacing:.5px}
.intro{left:215px;top:696px;width:770px;text-align:center;font-size:11px;line-height:22px;color:var(--muted)}
.service{width:260px;text-align:center}
.service-ring{width:172px;height:172px;border-radius:50%;border:1px solid #999;margin:0 auto;display:flex;align-items:center;justify-content:center}
.service-art{width:160px;height:160px;border-radius:50%}
.service-name{margin-top:18px;font-size:12px;font-weight:700;letter-spacing:.3px}
.service-desc{margin:12px auto 0;width:190px;font-size:11px;line-height:20px;color:var(--muted)}
.service-btn{margin:18px auto 0;width:130px;height:38px;border:1px solid;font-size:11px;display:flex;align-items:center;justify-content:center;letter-spacing:.3px}

/* about */
.about-photo{left:0;top:1178px;width:616px;height:398px;background:linear-gradient(120deg,#c9c2b6,#8b7a6a 45%,#3d5e86 100%)}
.about-panel{left:616px;top:1178px;width:584px;height:398px;background:var(--pale)}
.about-title{left:683px;top:1305px;font-size:18px;font-weight:700}
.about-text{left:683px;width:450px;font-size:11px;line-height:22px;color:#555}
.read-more{left:683px;top:1480px;font-size:12px;font-weight:600;color:var(--teal)}

/* gallery */
.filters{top:1690px;left:0;width:1200px;display:flex;justify-content:center;gap:30px;font-size:11px;color:#555;align-items:center}
.filter-active{background:var(--sky);color:var(--white);padding:2px 14px;border-radius:2px}
.tile{width:287px;height:246px}

/* feedback */
.feedback{left:0;top:2313px;width:1200px;height:432px;background:linear-gradient(180deg,#7fc0df,#5aa9d0)}
.feedback-title{top:2348px;color:var(--white)}
.quote-card{top:2402px;width:443px;height:213px;background:var(--white);padding:28px 24px}
.quote-photo{position:absolute;left:24px;top:50px;width:100px;height:115px}
.quote-text{position:absolute;left:137px;top:40px;width:284px;font-size:11px;line-height:21px;color:#444}
.quote-name{position:absolute;right:22px;top:145px;text-align:right;font-size:11px;line-height:14px;color:#444}
.quote-name b{font-weight:600;display:block}
.pager{top:2663px;width:30px;height:30px;background:var(--white);border:1px solid #ccc;display:flex;align-items:center;justify-content:center}

/* footer */
.site-footer{left:0;top:2745px;width:1200px;height:434px;background:var(--foot)}
.foot-head{top:2796px;font-size:15px;color:var(--sky);font-weight:500}
.foot-list{top:2836px;font-size:11px;line-height:28px;color:var(--foot-text)}
.foot-list .current{color:var(--sky)}
.contact-line{font-size:11px;line-height:25px;color:var(--foot-text)}
.newsletter{left:775px;top:2870px;width:296px;height:42px;display:flex}
.newsletter-input{flex:1;background:#222a30;color:#ccc;font-size:11px;display:flex;align-items:center;gap:10px;padding-left:14px}
.newsletter-btn{width:100px;background:var(--sky);color:var(--white);font-size:10px;font-weight:600;display:flex;align-items:center;justify-content:center}
.social{top:2938px;width:32px;height:32px;border-radius:50%}
.foot-rule{left:134px;top:3096px;width:930px;height:1px;background:#2a3036}
.copyright{left:0;top:3118px;width:1200px;text-align:center;font-size:11px;color:var(--foot-text)}
</style>
</head>
<body>

<header class="site-header">
  <a class="abs btn-consult" href="#">
    <svg width="12" height="11" viewBox="0 0 12 11"><rect x="0" y="0" width="12" height="8" rx="1" fill="#123"/><path d="M3 8 L3 11 L6 8Z" fill="#123"/></svg>
    FREE CONSULT
  </a>
  <div class="abs brand">
    <span class="brand-name">KDV</span>
    <span class="brand-sub">BY MOIRA TALLOW</span>
  </div>
  <a class="abs btn-phone" href="#">
    <svg width="12" height="12" viewBox="0 0 24 24"><path d="M6.6 10.8a15 15 0 0 0 6.6 6.6l2.2-2.2c.3-.3.7-.4 1-.2 1.1.4 2.3.6 3.6.6.6 0 1 .4 1 1V20c0 .6-.4 1-1 1A17 17 0 0 1 3 4c0-.6.4-1 1-1h3.5c.6 0 1 .4 1 1 0 1.3.2 2.5.6 3.6.1.3 0 .7-.2 1z" fill="#222"/></svg>
    555-014-2276
  </a>
  <nav class="abs nav" style="left:0;width:1200px">
    <a href="#" style="left:200px">Home</a>
    <a href="#" style="left:261px">About Us</a>
    <a href="#" style="left:337px">Treatments</a>
    <a href="#" style="left:430px">Financing</a>
    <a href="#" style="left:666px">Gallery</a>
    <a href="#" style="left:733px">Testimonials</a>
    <a href="#" style="left:832px">Blog</a>
    <a href="#" style="left:885px">FAQ</a>
    <a href="#" style="left:937px">Contact Us</a>
  </nav>
</header>

<section>
  <div class="abs hero" role="img" aria-label="Photo of a confident bald man in a suit and tie standing in front of an office building"></div>
  <h1 class="abs hero-title">INTRODUCING SCALP MICRO PIGMENTATION</h1>
  <p class="abs hero-text">Lumen has a long history of providing fantastic KDV results. Our unique, and most advanced Scalp Pigmentation technique provides you with the best result possible.</p>
  <a class="abs hero-btn" href="#">View Our Results</a>
  <svg class="abs hero-arrow" style="left:96px" width="14" height="26" viewBox="0 0 14 26"><path d="M12 2 L2 13 L12 24" fill="none" stroke="#fff" stroke-width="1.5"/></svg>
  <svg class="abs hero-arrow" style="left:1082px" width="14" height="26" viewBox="0 0 14 26"><path d="M2 2 L12 13 L2 24" fill="none" stroke="#fff" stroke-width="1.5"/></svg>
</section>

<section>
  <h2 class="abs section-title" style="top:655px">WHAT WE DO</h2>
  <p class="abs intro">Lorem ipsum dolor sit amet, consectetur adipiscing elit. Aenean commodo ligula eget dolor. Aenean massa. Cum sociis natoque penatibus et magnis dis parturient montes, nascetur ridiculus mus. Donec quam felis, ultricies nec</p>

  <div class="abs service" style="left:145px;top:780px">
    <div class="service-ring"><div class="service-art" role="img" aria-label="Line drawing of a head with a restored hairline" style="background:var(--blue)"></div></div>
    <div class="service-name">HAIRLINE</div>
    <p class="service-desc">Restore your receded hairline with scalp micropigmentation.</p>
    <a class="service-btn" href="#" style="border-color:var(--blue);color:var(--blue)">SEE RESULTS</a>
  </div>
  <div class="abs service" style="left:452px;top:780px">
    <div class="service-ring"><div class="service-art" role="img" aria-label="Line drawing of a head showing pattern baldness" style="background:var(--orange)"></div></div>
    <div class="service-name">PATTERN BALDNESS</div>
    <p class="service-desc">Strengthen and add density to thinning areas for the appearance of thick, strong hair.</p>
    <a class="service-btn" href="#" style="border-color:var(--orange);color:var(--orange)">SEE RESULTS</a>
  </div>
  <div class="abs service" style="left:766px;top:780px">
    <div class="service-ring"><div class="service-art" role="img" aria-label="Line drawing of a head with a transplant scar" style="background:var(--olive)"></div></div>
    <div class="service-name">SCAR CAMOUFLAGE</div>
    <p class="service-desc" style="width:220px">Conceal the visibility of your hair transplant (FUE/FUT) scar with small, color matched hair follicle</p>
    <a class="service-btn" href="#" style="border-color:var(--olive);color:var(--olive)">SEE RESULTS</a>
  </div>
</section>

<section>
  <div class="abs about-photo" role="img" aria-label="Photo of a practitioner applying scalp micropigmentation to a seated client"></div>
  <div class="abs about-panel"></div>
  <h2 class="abs about-title">ABOUT KDV</h2>
  <p class="abs about-text" style="top:1350px">Lorem ipsum dolor sit amet, consectetur adipisicing elit, sed do eiusmod tempor incididunt ut labore et dolore magna aliqua. Ut enim ad minim veniam, quis nostrud exercitation ullamco laboris nisi ut aliquip ex ea commodo consequat</p>
  <p class="abs about-text" style="top:1395px;display:none"></p>
  <p class="abs about-text" style="top:1420px">Lorem ipsum dolor sit amet, consectetur adipisicing elit, sed do eiusmod tempor incididunt ut labore et dolore magna aliqua. Ut enim ad minim veniam,</p>
  <a class="abs read-more" href="#">Read more</a>
</section>

<section>
  <h2 class="abs section-title" style="top:1638px">GALLERY</h2>
  <div class="abs filters">
    <span class="filter-active">All</span><span>Bald, Shaved Look</span><span>Scalp Scar</span><span>Thinning Hair</span><span>Female KDV</span>
  </div>
  <div class="abs tile" style="left:148px;top:1742px;background:linear-gradient(135deg,#d8dde2,#8f9aa4 60%,#3f4a55)" role="img" aria-label="Photo of an artist treating a client's scalp in the studio"></div>
  <div class="abs tile" style="left:459px;top:1742px;background:linear-gradient(135deg,#c7b9a8,#7d6a5c 50%,#3b6a9a)" role="img" aria-label="Photo of a practitioner marking a client's hairline"></div>
  <div class="abs tile" style="left:772px;top:1742px;background:linear-gradient(135deg,#b9b1a8,#6e6560 55%,#2d2c2e)" role="img" aria-label="Photo of a client checking his result in a hand mirror"></div>
  <div class="abs tile" style="left:148px;top:2010px;background:linear-gradient(135deg,#f2ece4,#d7b79a 50%,#4a5058)" role="img" aria-label="Before and after photo of a client's shaved head"></div>
  <div class="abs tile" style="left:459px;top:2010px;background:linear-gradient(135deg,#6c8fb8,#4c4a4a 55%,#1f2226)" role="img" aria-label="Photo of a client lying down during a treatment session"></div>
  <div class="abs tile" style="left:772px;top:2010px;background:linear-gradient(135deg,#b06a58,#5a3a34 50%,#25201f)" role="img" aria-label="Photo of a gloved artist working on a client's scalp"></div>
</section>

<section>
  <div class="abs feedback" role="img" aria-label="Faded background photo of a scalp treatment tinted blue"></div>
  <h2 class="abs section-title feedback-title">CLIENTS FEEDBACK</h2>
  <article class="abs quote-card" style="left:148px">
    <div class="quote-photo" style="background:linear-gradient(135deg,#a27a5e,#5b4030)" role="img" aria-label="Portrait photo of a smiling client"></div>
    <p class="quote-text">"Dorian is a full time Internet Marketing Analyst and Strategist. Her brain is an ocean of ideas and creativeness, and she loves expressing and sharing those ideas on her writings and artworks. Good service provider."</p>
    <p class="quote-name"><b>Tovin Marsh</b>C.E.O. Brightfold Labs Ltd</p>
  </article>
  <article class="abs quote-card" style="left:616px">
    <div class="quote-photo" style="background:linear-gradient(135deg,#8ab0b0,#8a6a5a)" role="img" aria-label="Portrait photo of a client with a shaved head"></div>
    <p class="quote-text">"Dorian is a full time Internet Marketing Analyst and Strategist. Her brain is an ocean of ideas and creativeness, and she loves expressing and sharing those ideas on her writings and artworks. Good service provider."</p>
    <p class="quote-name"><b>Elric Vane</b>C.E.O Quillmere Studio ltd</p>
  </article>
  <a class="abs pager" href="#" style="left:567px"><svg width="6" height="8" viewBox="0 0 6 8"><path d="M5 0 L1 4 L5 8" fill="none" stroke="#555"/></svg></a>
  <a class="abs pager" href="#" style="left:603px"><svg width="6" height="8" viewBox="0 0 6 8"><path d="M1 0 L5 4 L1 8" fill="none" stroke="#555"/></svg></a>
</section>

<footer>
  <div class="abs site-footer"></div>

  <h3 class="abs foot-head" style="left:134px">Contact Information</h3>
  <svg class="abs" style="left:134px;top:2843px" width="11" height="14" viewBox="0 0 12 16"><path d="M6 0a6 6 0 0 0-6 6c0 4.5 6 10 6 10s6-5.5 6-10a6 6 0 0 0-6-6zm0 8.5a2.5 2.5 0 1 1 0-5 2.5 2.5 0 0 1 0 5z" fill="var(--sky)"/></svg>
  <p class="abs contact-line" style="left:160px;top:2836px">Studio Row, Eastfield, 2nd block<br>4821 Harbor Lane, floor 2</p>
  <p class="abs contact-line" style="left:160px;top:2907px"><span style="color:#ccc">Email:</span> hello@kdvstudio.test<br><span style="color:#ccc">Phone:</span> 5550 142 276</p>

  <h3 class="abs foot-head" style="left:405px">Navigation</h3>
  <ul class="abs foot-list" style="left:405px;list-style:none">
    <li>Home</li><li>About us</li><li>Services</li><li>pages</li><li>Blog</li><li class="current">Careers</li><li>Contact</li>
  </ul>

  <h3 class="abs foot-head" style="left:632px">Services</h3>
  <ul class="abs foot-list" style="left:632px;list-style:none">
    <li>Hairline</li><li>Pattern Baldness</li><li>scar camouflage</li>
  </ul>

  <h3 class="abs foot-head" style="left:775px">Newsletter</h3>
  <p class="abs contact-line" style="left:775px;top:2836px">Enter your email &amp; subscribing newsletter</p>
  <form class="abs newsletter">
    <span class="newsletter-input">
      <svg width="12" height="9" viewBox="0 0 12 9"><rect x=".5" y=".5" width="11" height="8" fill="none" stroke="#bbb"/><path d="M.5 .5 L6 5 L11.5 .5" fill="none" stroke="#bbb"/></svg>
      Email address
    </span>
    <span class="newsletter-btn">SUBSCRIBE</span>
  </form>
  <span class="abs social" style="left:775px;background:#3b5b98"></span>
  <span class="abs social" style="left:815px;background:#3aa0dc"></span>
  <span class="abs social" style="left:855px;background:#d34836"></span>

  <div class="abs foot-rule"></div>
  <p class="abs copyright">2017 © KDV.com. All rights reserved</p>
</footer>

</body>
</html>
```